Business Card Design

We are a manufacturing and distribution company with most of our customer base being supermarkets. We have established brand guidelines that are attached.

```html
<!DOCTYPE html>
<html lang="en">
<head>
<meta charset="utf-8">
<title>Valmore Business Card</title>
<link rel="stylesheet" href="https://fonts.googleapis.com/css2?family=Montserrat:wght@400;500;800&display=swap">
<style>
  :root {
    --backdrop: #c9c9c9;
    --card-white: #ffffff;
    --ink: #1e1e1e;
    --brand-red: #e01e2b;
    --brand-blue: #0f63a8;
    --gradient-mid: #6b4470;
    --shadow: rgba(0, 0, 0, 0.35);
  }
  * { box-sizing: border-box; margin: 0; padding: 0; }
  html, body { width: 1200px; height: 900px; overflow: hidden; }
  body {
    background: var(--backdrop);
    font-family: "Montserrat", Arial, sans-serif;
    position: relative;
  }
  .card {
    position: absolute;
    width: 520px;
    height: 300px;
    border-radius: 26px;
    box-shadow: 0 10px 24px var(--shadow);
    overflow: hidden;
  }
  .card-front {
    left: 70px;
    top: 120px;
    background: linear-gradient(195deg, var(--brand-red) 0%, var(--gradient-mid) 48%, var(--brand-blue) 100%);
    display: flex;
    align-items: center;
    justify-content: center;
    gap: 16px;
  }
  .brand-square {
    width: 22px;
    height: 22px;
    background: var(--card-white);
  }
  .brand-name {
    font-weight: 800;
    font-size: 40px;
    letter-spacing: 3px;
    color: var(--card-white);
  }
  .card-back {
    left: 610px;
    top: 470px;
    background: var(--card-white);
  }
  .card-back .brand-lockup {
    position: absolute;
    left: 38px;
    top: 44px;
    display: flex;
    align-items: center;
    gap: 14px;
  }
  .card-back .brand-square { background: var(--brand-red); }
  .card-back .brand-name { color: var(--ink); font-size: 36px; }
  .contact-person {
    position: absolute;
    left: 38px;
    top: 128px;
    color: var(--ink);
  }
  .person-name {
    font-weight: 800;
    font-size: 19px;
    letter-spacing: 0.5px;
  }
  .person-name .first { color: var(--brand-red); }
  .person-name .last { color: var(--brand-blue); }
  .person-role { font-size: 14px; font-weight: 500; margin-top: 2px; }
  .contact-list { list-style: none; margin-top: 14px; }
  .contact-list li {
    display: flex;
    align-items: center;
    gap: 8px;
    font-size: 14px;
    line-height: 21px;
  }
  .contact-list svg { width: 13px; height: 13px; fill: var(--brand-blue); }
  .web-domain { color: var(--brand-red); }
  .address {
    position: absolute;
    right: 32px;
    top: 214px;
    text-align: right;
    font-size: 13px;
    line-height: 19px;
    color: var(--ink);
  }
</style>
</head>
<body>
  <section class="card card-front">
    <span class="brand-square"></span>
    <span class="brand-name">VALMORE</span>
  </section>

  <section class="card card-back">
    <div class="brand-lockup">
      <span class="brand-square"></span>
      <span class="brand-name">VALMORE</span>
    </div>

    <div class="contact-person">
      <p class="person-name"><span class="first">DANIEL</span> <span class="last">REED</span></p>
      <p class="person-role">Managing Director</p>
      <ul class="contact-list">
        <li>
          <svg viewBox="0 0 16 16" aria-hidden="true"><path d="M3.5 1l2.5 3-1.5 1.8c.8 1.9 2.3 3.4 4.2 4.2L10.5 8.5l3 2.5-1.5 3.5C6.5 14 2 9.5 1.5 3z"/></svg>
          055-210 338 417
        </li>
        <li>
          <svg viewBox="0 0 16 16" aria-hidden="true"><path d="M1 3h14v10H1z M2 4l6 5 6-5" fill="none" stroke="#0f63a8" stroke-width="1.6"/></svg>
          hello@valmore.co
        </li>
        <li>
          <svg viewBox="0 0 16 16" aria-hidden="true"><circle cx="8" cy="8" r="6.5" fill="none" stroke="#0f63a8" stroke-width="1.4"/><path d="M1.5 8h13M8 1.5c-3 3.5-3 9.5 0 13M8 1.5c3 3.5 3 9.5 0 13" fill="none" stroke="#0f63a8" stroke-width="1.2"/></svg>
          <span>www.<span class="web-domain">valmore</span>.co</span>
        </li>
      </ul>
    </div>

    <p class="address">88, Harbor Lane Works<br>30917, Eastland</p>
  </section>
</body>
</html>
```